Business Card Design Project Massage Shop

Business card for Foot, Hot Stone and Full body Massage. I am thinking photo for the front. Back should say "$20 off 1hr basic service" "Offer not valid with any other coupons or offers"

Target Market(s)

Women wanting good quality massage

Industry/Entity Type

Business

Contact Information for Business Card

816.472.3908
27815 W 12 Hwy
Independence Mo 64055

www.lanternmassage.co

Other font styles liked:
• http://www.typequarry.net/fonts/brelwick/no.-seven/

Colors
0455a3

Requirements
Must have
• The business name "Lantern Massage" must be in this font and a royal blue color http://www.typequarry.net/fonts/brelwick/no.-seven/
• The remaining information must be more readable.
Should not have
• the web site is .co
• Not a .com
• should not look like it was done on a prindle or someothere website.

```html
<!DOCTYPE html>
<html lang="en">
<head>
<meta charset="utf-8">
<title>Lantern Massage – Business Card</title>
<link rel="stylesheet" href="https://fonts.googleapis.com/css2?family=Open+Sans:wght@400;600;700&family=Jost:wght@500;600&display=swap">
<style>
  :root {
    --canvas: #ece8e2;
    --card-white: #fbfbfb;
    --orange: #e8842a;
    --royal-blue: #0455a3;
    --ink: #1a1a1a;
    --photo-skin: #d9b39a;
    --photo-towel: #e6ddd2;
    --photo-green: #8fb77a;
    --photo-dark: #2a2a22;
  }
  * { box-sizing: border-box; margin: 0; padding: 0; }
  html, body { width: 1200px; height: 800px; overflow: hidden; }
  body {
    background: var(--canvas);
    font-family: "Open Sans", Arial, sans-serif;
    color: var(--ink);
    position: relative;
  }
  .card {
    position: absolute;
    width: 560px;
    height: 320px;
    border-radius: 4px;
    overflow: hidden;
    box-shadow: 0 10px 24px rgba(60, 45, 30, 0.18);
    background: var(--card-white);
  }

  /* Offer side */
  .card--offer { left: 580px; top: 60px; }
  .offer__photo {
    position: absolute; inset: 0;
    background:
      radial-gradient(ellipse at 30% 25%, var(--photo-skin) 0%, rgba(217,179,154,0) 45%),
      radial-gradient(ellipse at 75% 30%, var(--photo-green) 0%, rgba(143,183,122,0) 50%),
      linear-gradient(170deg, #efe7dc 0%, var(--photo-towel) 45%, #a38f78 100%);
  }
  .offer__panel {
    position: absolute;
    top: 26px; right: 26px; bottom: 0;
    width: 190px;
    background: var(--orange);
    padding: 36px 18px 0 22px;
    text-align: center;
  }
  .offer__edge {
    position: absolute; top: 26px; right: 0; bottom: 0; width: 26px;
    background: linear-gradient(180deg, var(--photo-dark) 0%, var(--photo-green) 60%, #6e8f5c 100%);
  }
  .offer__amount {
    font-family: "Jost", "Futura", sans-serif;
    font-weight: 600;
    font-size: 52px;
    line-height: 0.9;
    color: var(--ink);
  }
  .offer__amount-off { display: block; font-size: 42px; letter-spacing: 1px; }
  .offer__rule { border: 0; border-top: 1px solid var(--ink); margin: 8px 0; }
  .offer__service { font-size: 17px; font-weight: 600; }
  .offer__terms { font-size: 12px; line-height: 1.3; font-style: italic; }
  .offer__social { display: flex; justify-content: center; gap: 10px; margin-top: 10px; }
  .offer__social-mark { width: 18px; height: 18px; background: var(--ink); border-radius: 2px; }

  /* Contact side */
  .card--contact { left: 60px; top: 410px; }
  .contact__waves { position: absolute; inset: 0; }
  .contact__brand {
    position: absolute; left: 40px; top: 60px;
    display: flex; align-items: center; gap: 12px;
  }
  .contact__brand-dot { width: 26px; height: 26px; border-radius: 50%; background: var(--orange); }
  .contact__brand-name { font-size: 30px; font-weight: 600; color: var(--royal-blue); }
  .contact__person { position: absolute; right: 40px; top: 120px; text-align: right; }
  .contact__name { font-size: 30px; font-weight: 600; color: var(--orange); line-height: 1.1; }
  .contact__role { font-size: 17px; }
  .contact__details { position: absolute; left: 180px; top: 212px; }
  .contact__phone { font-size: 32px; font-weight: 700; line-height: 1.1; }
  .contact__web { font-size: 21px; font-weight: 600; }
  .contact__address { font-size: 15px; }
</style>
</head>
<body>

  <section class="card card--offer">
    <div class="offer__photo" role="img" aria-label="Photo of a relaxed woman on a spa towel with stacked hot stones and green leaves"></div>
    <div class="offer__panel">
      <p class="offer__amount">$20<span class="offer__amount-off">OFF</span></p>
      <hr class="offer__rule">
      <p class="offer__service">1hr basic service</p>
      <hr class="offer__rule">
      <p class="offer__terms">Offer not valid with any other coupons or offers</p>
      <hr class="offer__rule">
      <div class="offer__social">
        <span class="offer__social-mark"></span>
        <span class="offer__social-mark"></span>
      </div>
    </div>
    <div class="offer__edge"></div>
  </section>

  <section class="card card--contact">
    <svg class="contact__waves" viewBox="0 0 560 320" width="560" height="320" aria-hidden="true">
      <path d="M0,150 C150,205 330,185 560,205 L560,320 L0,320 Z" fill="var(--orange)"/>
      <path d="M0,165 C150,215 320,200 520,212" fill="none" stroke="var(--card-white)" stroke-width="2"/>
      <path d="M20,120 C60,150 200,160 430,200" fill="none" stroke="var(--orange)" stroke-width="3"/>
      <path d="M12,100 C30,150 130,175 250,178 C150,182 40,165 12,100 Z" fill="var(--royal-blue)"/>
    </svg>

    <div class="contact__brand">
      <span class="contact__brand-dot"></span>
      <span class="contact__brand-name">Lantern Massage</span>
    </div>

    <div class="contact__person">
      <p class="contact__name">Dana Whitfield</p>
      <p class="contact__role">Masseuse</p>
    </div>

    <div class="contact__details">
      <p class="contact__phone">816.472.3908</p>
      <p class="contact__web">www.lanternmassage.co</p>
      <p class="contact__address">27815 W 12 Hwy, Independence Mo 64055</p>
    </div>
  </section>

</body>
</html>
```